Bramwell Builders Web Site / Business Cards

Construction Company that specializes in Water and Fire Damage, Residential ReModels, Landscaping and Building ADU (Accessory Dwelling Unit)

Growing and changing families often need additional space, and a remodeling project can often provide that. Adding a new area, or repurposing an existing one can satisfy this requirement.

Other times, homeowners want to update the look in their kitchen or bathroom with more than just a change of cabinetry or vanity doors and drawers. Whatever your needs are, Bramwell Builders has skilled workers who are bonded and insured, and ready to make your dreams and visions a reality.

Target Market(s)

Home Owners

Industry/Entity Type

Construction Company

Contact Information for Business Card

Center Logo with our information on the corners

Back side to be Logo Only
Contact Info
SBRQ License # 5820914
info@bramwellbuildersca.example
www.bramwellbuildersca.example

Coding

Coded - Design and coding required

Number of Pages Required

5+ page

Font styles to use
Serif
Sans Serif

Requirements
Must have
• Using our Logo Colors
Home
About Us
Services
Projects / Portfolio
Contact Us
Nice to have
• Colors matching our Logo
Should not have
• Black because it doesnt match our logo

```html
<!DOCTYPE html>
<html lang="en">
<head>
<meta charset="UTF-8">
<title>Bramwell Builders – Business Cards</title>
<link rel="stylesheet" href="https://fonts.googleapis.com/css2?family=Poppins:wght@500;700&display=swap">
<style>
  :root {
    --backdrop: #e6e4e1;
    --card: #f5f5f3;
    --ink: #1f1f1f;
    --accent: #e8641b;
    --card-shadow: 0 14px 30px rgba(60, 50, 40, 0.18);
  }
  * { box-sizing: border-box; margin: 0; padding: 0; }
  html, body {
    width: 1200px;
    height: 900px;
    overflow: hidden;
    background: var(--backdrop);
    font-family: "Poppins", sans-serif;
    color: var(--ink);
  }
  .sheet {
    width: 1200px;
    height: 900px;
    display: flex;
    flex-direction: column;
    align-items: center;
    justify-content: center;
    gap: 60px;
  }
  .card {
    position: relative;
    width: 630px;
    height: 360px;
    background: var(--card);
    box-shadow: var(--card-shadow);
  }
  .brand {
    position: absolute;
    left: 50%;
    top: 50%;
    transform: translate(-50%, -50%);
    display: flex;
    align-items: center;
    gap: 14px;
    white-space: nowrap;
  }
  .brand-square {
    width: 26px;
    height: 26px;
    background: var(--accent);
  }
  .brand-name {
    font-weight: 700;
    font-size: 34px;
    letter-spacing: 0.5px;
    color: var(--ink);
  }
  .card--back .brand-name { font-size: 30px; }
  .card--back .brand-square { width: 22px; height: 22px; }
  .contact {
    position: absolute;
    font-weight: 500;
    font-size: 14px;
    letter-spacing: 0.2px;
    white-space: nowrap;
  }
  .contact--license {
    right: 22px;
    top: 24px;
    writing-mode: vertical-rl;
  }
  .contact--email {
    left: 22px;
    bottom: 24px;
    writing-mode: vertical-rl;
    transform: rotate(180deg);
  }
  .contact--web {
    left: 50%;
    bottom: 28px;
    transform: translateX(-50%);
  }
</style>
</head>
<body>
  <main class="sheet">
    <section class="card card--front" aria-label="Business card front">
      <div class="brand">
        <span class="brand-square"></span>
        <span class="brand-name">Bramwell Builders</span>
      </div>
    </section>

    <section class="card card--back" aria-label="Business card back">
      <div class="brand">
        <span class="brand-square"></span>
        <span class="brand-name">Bramwell Builders</span>
      </div>
      <p class="contact contact--license">SBRQ License # 5820914</p>
      <p class="contact contact--email">info@bramwellbuildersca.example</p>
      <p class="contact contact--web">www.bramwellbuildersca.example</p>
    </section>
  </main>
</body>
</html>
```